Silver Kettle Studio Marketing Postcard

I need a 2 sided A6 postcard to distribute to potential clients. The postcard will include the business logo and information about the service we provide and contact information. I want it to be stylish and to compliment the business card. I've attached the business card and logo files as well as some text to use. I have other source files (.eps and.ai) if required please message me. I don't need the postal address or my position included on the postcard.
I am open to portrait or landscape designs, whatever you think is most stylish and eye catching.

```html
<!DOCTYPE html>
<html lang="en">
<head>
<meta charset="utf-8">
<title>Silver Kettle Studio – Postcard</title>
<link rel="stylesheet" href="https://fonts.googleapis.com/css2?family=Archivo+Black&family=Arimo:wght@700&family=Inter:wght@300;400;700&display=swap">
<style>
  :root {
    --backdrop: #6e706f;
    --paper: #ffffff;
    --ink: #1e1e1e;
    --green: #76b043;
    --green-text: #6fae3d;
    --font-body: "Inter", Helvetica, Arial, sans-serif;
    --font-display: "Archivo Black", "Arial Black", sans-serif;
    --font-strong: "Arimo", Helvetica, Arial, sans-serif;
  }
  * { box-sizing: border-box; margin: 0; padding: 0; }
  html, body { width: 880px; height: 1200px; overflow: hidden; }
  body { background: var(--backdrop); font-family: var(--font-body); color: var(--ink); position: relative; }

  .postcard {
    position: absolute; left: 84px; top: 90px; width: 711px; height: 1001px;
    background: var(--paper);
  }
  .intro {
    position: absolute; left: 53px; top: 48px; width: 620px;
    font-size: 19.5px; font-weight: 300; line-height: 26.3px; letter-spacing: -0.1px;
  }
  .intro strong { font-family: var(--font-display); font-weight: 400; font-size: 18.5px; }

  .questions {
    position: absolute; left: 53px; top: 224px; width: 608px; height: 389px;
  }
  .questions-frame { position: absolute; inset: 0; }
  .questions-title {
    position: absolute; left: 39px; top: 20px;
    font-family: var(--font-display); font-size: 19px; color: var(--green-text);
  }
  .question-list { position: absolute; left: 33px; top: 64px; width: 560px; list-style: none; }
  .question-list li {
    position: relative; padding-left: 36px;
    font-size: 19.5px; font-weight: 300; line-height: 24.5px;
  }
  .question-list li + li { margin-top: 16px; }
  .question-list svg { position: absolute; left: 0; top: 2px; width: 22px; height: 26px; }

  .call-out {
    position: absolute; left: 61px; top: 636px;
    font-family: var(--font-display); font-size: 19px; line-height: 26px; color: var(--green-text);
  }

  .contact-band {
    position: absolute; left: 0; top: 700px; width: 711px; height: 158px;
    background: var(--green); padding: 14px 0 0 61px;
    font-size: 19.5px; font-weight: 300; line-height: 26px; color: #111;
  }
  .contact-band strong { font-weight: 700; }

  .footer { position: absolute; left: 0; top: 878px; width: 711px; text-align: center; }
  .footer-tagline { font-family: var(--font-strong); font-weight: 700; font-size: 21.5px; line-height: 28px; }
  .footer-address { font-size: 19.5px; font-weight: 300; margin-top: 4px; }
  .footer-web { font-size: 22px; font-weight: 400; margin-top: 14px; letter-spacing: 0.3px; }
  .footer-web span { font-family: var(--font-display); color: var(--green-text); font-size: 21px; }
</style>
</head>
<body>
<svg width="0" height="0" style="position:absolute">
  <defs>
    <symbol id="mouse-icon" viewBox="0 0 22 26">
      <path d="M8 2 C4 1 2 4 4 7" fill="none" stroke="#76b043" stroke-width="1.8" stroke-linecap="round"/>
      <rect x="3" y="7" width="16" height="18" rx="8" fill="#76b043" transform="rotate(-25 11 16)"/>
      <path d="M7 12 L15 9" stroke="#fff" stroke-width="1.4" transform="rotate(0)"/>
    </symbol>
  </defs>
</svg>

<main class="postcard">
  <p class="intro">Most of us have multiple digital devices at home and the more devices we accumulate the harder it is to manage them. This is where <strong>Silver Kettle Studio can help</strong>. From computers to cordless phones to home networks. We provide on site setup, support and education for all the devices in your life. We currently service East, Inner West, South and Lower North areas of Sydney.</p>

  <section class="questions">
    <svg class="questions-frame" viewBox="0 0 608 389" preserveAspectRatio="none" aria-hidden="true">
      <rect x="1" y="1" width="606" height="387" fill="none" stroke="#76b043" stroke-width="2" stroke-dasharray="10 7"/>
    </svg>
    <h2 class="questions-title">Ask yourself the following questions.</h2>
    <ul class="question-list">
      <li><svg><use href="#mouse-icon"/></svg>Do your devices work as you would like them to?</li>
      <li><svg><use href="#mouse-icon"/></svg>Are they ‘talking’ to each other (connected) as they should be?</li>
      <li><svg><use href="#mouse-icon"/></svg>Do you get confused when trying to change a setting on your TV, computer, home network or mobile device?</li>
      <li><svg><use href="#mouse-icon"/></svg>Does online security concern you?</li>
      <li><svg><use href="#mouse-icon"/></svg>Are you not sure what to buy?</li>
      <li><svg><use href="#mouse-icon"/></svg>Do you dread opening the box reading the manual and setting everything up?</li>
    </ul>
  </section>

  <p class="call-out">If you answered YES to any of these questions then<br>help is only a call or email away.</p>

  <section class="contact-band">
    <p>Silver Kettle Studio has 20 years experience dealing with a<br>large range of technology. Drop me a line on <strong>0491570186</strong> or<br>send an email to <strong>info@silverkettle.com.au</strong>.<br><strong>Telephone conversations are free.</strong> Once we have<br>discussed your needs we can make a time for an appointment.</p>
  </section>

  <footer class="footer">
    <p class="footer-tagline">On site Home Digital Services in Sydney, Australia</p>
    <p class="footer-address">Rowan Ashby, PO Box 14, Elmwood NSW 2099</p>
    <p class="footer-web">WWW.<span>SILVERKETTLE</span>.COM.AU</p>
  </footer>
</main>
</body>
</html>
```